Lena Hartwell Web

Lena Hartwell is a singer/songwriter that has a presence in the market for over 20 years. She currently has a website, lenahartwell.example that needs a major makeover. IT needs to be reorganized to; 1) make it more user friendly; 2) enable multi-languages including; Spanish, French, Russian, Japanese, Chinese and Portuguese; 3) enable purchases online through a storefront of promotional merchandise and music tracks. She has a logo that needs an update, as well as we currently have a business card open on PixelBazaar for input. Working to re-brand, or refresh her brand.

Lena Hartwell is the next Rosa Delmont! She has 5 platinum records, Lumen Award nominations and tours with Harold Prescott globally and is Nora Vandermeer's key backup singer for 12 years.
Updates

Some common questions have come up.  Here is some further input:

1) Colors - No specific color in mind but probably earth tones.  Although at this point we''re completely open.  Mary likes classical style, Russian, French decor.  Paris architecture. Greek, Italian textures, Goddess like symbols from the Roman Empire, or the symbols and pomp of the British monarchy.  One name on tap for the new CD is "Lanterns Over Quiet Water"
2) Example website - I have not found a new one specifically, but what I don''t like about the existing one is it is not easy to navigate.  Needs to be streamlined and easy to navigate with a storefront for merchandise and music downloads.  
3) On Logo - We''re revamping a "Global" merchandise rollout logo.  We''ve also considered possibly modifying the old english "Hartwell" family crest which signifies royalty, but have not explored that too much.  The hexagon yellow logo on her current website, I was thinking of modifying to gold (brushed - or polished?), then taking the LH lettering using a fountain pen type look there the line thickness flows with pressure on the pen, then make the gold look like a pillow, with the letter making an impression into the gold pillow.  This expands to a high quality pin, blinged up broach with diamonds imbedded for example, Global label identity, tee shirts, label tag on fashion clothing etc etc. 
 4) One thing marketing has asked us to build is a routine video blog to reach out to fans in a personal way.  Short clips of daily activity, travel prep for shows, etc. Possibly a signup/fanpage where people get emails sent back whenever anything new is posted, like a video blog, new pics, new events.  A menu to choose what you get updates on. 

Thanks, Dennis

Target Market(s)

1) Fan base in Europe, Asia, Latin America and North America
2) Movie producers seeking soundtracks
3) Private clients seeking an outstanding performer for corporate events

Industry/Entity Type

Singer

Requirements
Must have
• Better organization into smaller pages. Items critical include: 1) music tracks, 2) ClipStream links, 3) photos & Video, 4) storefront to enable online merchandise purchase 5) a way to illustrate her genre from; gospel, to rock, funk, R&B, country,

```html
<!DOCTYPE html>
<html lang="en">
<head>
<meta charset="utf-8">
<title>Lena Hartwell – Official Site</title>
<link rel="stylesheet" href="https://fonts.googleapis.com/css2?family=Roboto+Condensed:wght@400;700&family=EB+Garamond:ital@1&display=swap">
<style>
:root{
  --ink:#0b0c0e;
  --panel:#111315;
  --panel-edge:#2a2c2f;
  --footer:#0f1113;
  --text:#e9e9e9;
  --muted:#b8b8b8;
  --orange:#f0782a;
  --orange-light:#ff9a48;
  --orange-dark:#c8530e;
  --btn-text:#2a1204;
  --nav-top:#3b3d40;
  --nav-bottom:#17181a;
  --white:#ffffff;
}
*{box-sizing:border-box;margin:0;padding:0}
html,body{width:965px;height:1200px;overflow:hidden;background:var(--ink)}
body{font-family:"Roboto Condensed",Arial,sans-serif;color:var(--text)}
.page{position:relative;width:951px;height:1183px;transform:scale(1.0147,1.0144);transform-origin:0 0;overflow:hidden;background:var(--ink)}
.abs{position:absolute}

.backdrop{left:0;top:0;width:951px;height:915px;
  background:
    radial-gradient(ellipse 620px 150px at 475px 690px,rgba(255,255,255,.55),rgba(255,255,255,0) 70%),
    radial-gradient(ellipse 900px 260px at 475px 830px,#5a5c60,rgba(40,42,45,.6) 55%,rgba(0,0,0,0) 80%),
    radial-gradient(ellipse 700px 420px at 475px 460px,#2a2b2e,#060607 75%);}

.lang{left:726px;top:11px;width:103px;height:23px;border:1px solid #3a3b3e;border-radius:2px;background:#141517;font-size:10px;color:#9a9a9a;padding:5px 0 0 10px}
.lang svg{position:absolute;right:7px;top:8px}

.logo{left:150px;top:15px;width:134px;height:134px;border-radius:50%;background:var(--white);display:flex;align-items:center;justify-content:center;font-size:21px;color:#1a1a1a;font-weight:400}

.nav{left:368px;top:66px;display:flex;gap:5px}
.nav a{display:block;height:29px;padding:0 14px;line-height:29px;font-size:11px;color:var(--white);text-decoration:none;border-radius:2px;background:linear-gradient(var(--nav-top),var(--nav-bottom));}
.nav a.active{background:linear-gradient(#d4d4d4,#8c8c8c);color:#1a1a1a}

.about-title{left:134px;top:176px;font-family:"EB Garamond",Georgia,serif;font-style:italic;font-weight:400;font-size:23px;color:var(--white)}
.about-title span{color:var(--orange)}
.about-text{left:134px;top:215px;width:221px;height:225px;overflow:hidden;font-size:10px;line-height:12.6px;text-align:justify;color:var(--text)}
.about-text p{margin-bottom:12.6px}
.scrollbar{left:378px;top:225px;width:11px;height:213px;background:#e8e8e8;border:1px solid #999}
.scrollbar i{position:absolute;left:2px;top:88px;width:5px;height:36px;background:#666;border-radius:3px}

.btn{display:flex;align-items:center;justify-content:center;border-radius:3px;background:linear-gradient(var(--orange-light),var(--orange));color:var(--btn-text);font-weight:700;font-size:13.5px}
.purchase{left:172px;top:473px;width:153px;height:33px}

.tablet{left:470px;top:122px}
.dots{left:592px;top:560px;display:flex;gap:6px}
.dots i{width:8px;height:8px;border-radius:50%;background:#d8d8d8}
.dots i:first-child{background:var(--orange)}

.tabs{left:134px;top:616px;display:flex;gap:5px}
.tabs span{height:28px;line-height:28px;padding:0 14px;font-size:11px;border-radius:3px 3px 0 0;background:linear-gradient(var(--orange-light),var(--orange));color:#2a1204}
.tabs span.current{background:var(--panel);color:var(--white);padding:0 16px}
.media-panel{left:134px;top:644px;width:694px;height:236px;background:var(--panel);border:1px solid var(--panel-edge);border-top:0;border-radius:0 0 6px 6px}
.pager{width:23px;height:23px;border-radius:3px;background:linear-gradient(#f0f0f0,#bdbdbd);top:661px}
.pager svg{display:block;margin:7px auto 0}
.thumb{top:695px;width:206px;height:140px}
.thumb .play{position:absolute;left:90px;top:58px}
.caption{top:847px;font-size:11px;color:var(--orange)}

.footer{left:0;top:915px;width:951px;height:237px;background:var(--footer)}
.col-title{top:927px;font-size:14.5px;font-weight:400;color:var(--text);letter-spacing:.2px;line-height:17px}
.sound-drop{left:134px;top:959px;width:222px;height:32px;border-radius:3px;background:linear-gradient(#6a6b6d,#3e3f41);padding:3px 8px;font-size:11px;line-height:12px;color:var(--white)}
.sound-drop b{display:block;font-size:12px;color:#222}
.sound-drop em{position:absolute;right:8px;top:11px;font-style:normal;font-size:8px;color:#ddd}
.social-label{left:133px;top:1031px;font-size:14px;color:var(--text)}
.social{left:242px;top:1030px;display:flex;gap:2px}
.social span{height:20px;padding:0 2px;line-height:20px;font-size:7px;border-radius:3px;background:#2b2d30;color:var(--text);white-space:nowrap}
.gallery-tile{width:65px;height:61px}
.field{border:1px solid #2c2e31;background:#0b0c0d;font-size:10px;color:#aaa;padding:7px 9px}
.send{left:663px;top:1060px;width:106px;height:25px}
.legal{left:0;top:1152px;width:951px;height:31px;background:var(--orange-dark);text-align:center;line-height:31px;font-size:10.5px;color:var(--white)}
.legal span{color:#ffd79a}
</style>
</head>
<body>
<div class="page">
  <div class="abs backdrop" role="img" aria-label="Starfield sky with a glowing planet horizon"></div>

  <div class="abs lang">Select Language
    <svg width="8" height="6" viewBox="0 0 8 6"><path d="M0 0h8L4 6z" fill="#9a9a9a"/></svg>
  </div>

  <div class="abs logo">Lena Hartwell</div>

  <nav class="abs nav">
    <a class="active" href="#">Home</a>
    <a href="#">About</a>
    <a href="#">Events</a>
    <a href="#">Video</a>
    <a href="#">Pictures</a>
    <a href="#">Discographic</a>
    <a href="#">Contact</a>
  </nav>

  <h1 class="abs about-title">About <span>Lena Hartwell</span></h1>
  <div class="abs about-text">
    <p>Lena Hartwell displays the vocal prowess, attitude and range of a true ingenue. (Chartline Weekly)</p>
    <p>With a powerfully unique voice and a definitive sound, Lena Hartwell consistently delivers soul stirring performances that captivate audiences around the world. Using her past as a spring board, Lena channels memories into melodies that are proud and strong. Her rich melodic sound and exciting performance style are rooted in the story of a pastor's daughter with a passion for singing good music.</p>
    <p>With Meridian Records, Lena began singing for Movie soundtracks and was even featured in the movie Velvet Room where she portrayed the artist Celia Marsh and sang “Tap the Door” for the soundtrack. She performed “Eyes Across the Room” with Victor Lane for the closing credits of Midnight Ledger.</p>
  </div>
  <div class="abs scrollbar"><i></i></div>

  <a class="abs btn purchase">Purchase Music Track</a>

  <svg class="abs tablet" width="370" height="440" viewBox="0 0 370 440">
    <g transform="rotate(3 185 220)">
      <rect x="22" y="12" width="330" height="412" rx="22" fill="#e4e4e4" stroke="#bfbfbf" stroke-width="2"/>
      <circle cx="187" cy="32" r="3" fill="#555"/>
      <rect x="48" y="44" width="276" height="340" fill="#5a2466" role="img" aria-label="Singer performing on stage under purple lights"/>
      <circle cx="160" cy="214" r="16" fill="#ffffff" opacity=".8"/>
      <path d="M154 204v20l16-10z" fill="#777"/>
      <rect x="176" y="396" width="18" height="8" rx="4" fill="none" stroke="#aaa"/>
    </g>
  </svg>
  <div class="abs dots"><i></i><i></i><i></i><i></i><i></i></div>

  <div class="abs tabs">
    <span class="current">Latest Video</span>
    <span>Latest Events</span>
    <span>Latest Pictures</span>
  </div>
  <div class="abs media-panel"></div>
  <div class="abs pager" style="left:760px"><svg width="6" height="9" viewBox="0 0 6 9"><path d="M5 0L1 4.5 5 9" fill="none" stroke="#333" stroke-width="1.6"/></svg></div>
  <div class="abs pager" style="left:787px"><svg width="6" height="9" viewBox="0 0 6 9"><path d="M1 0l4 4.5L1 9" fill="none" stroke="#333" stroke-width="1.6"/></svg></div>

  <div class="abs thumb" style="left:150px;background:linear-gradient(135deg,#5a1f4a,#1c0d22)" role="img" aria-label="Video still of guitarist and singer on stage">
    <svg class="play" width="24" height="24" viewBox="0 0 24 24"><rect width="24" height="24" rx="3" fill="#d42a2a"/><path d="M9 6v12l9-6z" fill="#fff"/></svg>
  </div>
  <div class="abs thumb" style="left:376px;background:linear-gradient(135deg,#2a2520,#0a0a0a)" role="img" aria-label="Video still of singer beside a piano">
    <svg class="play" width="24" height="24" viewBox="0 0 24 24"><rect width="24" height="24" rx="3" fill="#d42a2a"/><path d="M9 6v12l9-6z" fill="#fff"/></svg>
  </div>
  <div class="abs thumb" style="left:604px;background:linear-gradient(135deg,#9a7a44,#2a1f10)" role="img" aria-label="Sepia video still of singer facing the crowd">
    <svg class="play" width="24" height="24" viewBox="0 0 24 24"><rect width="24" height="24" rx="3" fill="#d42a2a"/><path d="M9 6v12l9-6z" fill="#fff"/></svg>
  </div>
  <div class="abs caption" style="left:151px">Video Headig Goes Here</div>
  <div class="abs caption" style="left:376px">Video Headig Goes Here</div>
  <div class="abs caption" style="left:604px">Video Headig Goes Here</div>

  <footer class="abs footer"></footer>
  <h3 class="abs col-title" style="left:134px">QUICK LINKS</h3>
  <h3 class="abs col-title" style="left:375px">IMGAE GALLERY</h3>
  <h3 class="abs col-title" style="left:604px">CONTACT US</h3>

  <div class="abs sound-drop"><b>Sound Drop</b>Send your Sound<em>TuneVault</em></div>
  <div class="abs social-label">Social Media links :</div>
  <div class="abs social"><span>Chirper</span><span>ClipStream</span><span>Friendspace</span><span>RSS</span></div>

  <div class="abs gallery-tile" style="left:375px;top:958px;background:#6a6a6a" role="img" aria-label="Black and white portrait photo"></div>
  <div class="abs gallery-tile" style="left:446px;top:958px;background:#8a3a34" role="img" aria-label="Singer in red dress"></div>
  <div class="abs gallery-tile" style="left:516px;top:958px;background:#9a6a20" role="img" aria-label="Singer in red dress by a window"></div>
  <div class="abs gallery-tile" style="left:375px;top:1025px;background:#9a6a20" role="img" aria-label="Singer in warm light by a window"></div>
  <div class="abs gallery-tile" style="left:446px;top:1025px;background:#6a6a6a" role="img" aria-label="Black and white portrait photo"></div>
  <div class="abs gallery-tile" style="left:516px;top:1025px;background:#8a3a34" role="img" aria-label="Singer in red dress standing"></div>

  <div class="abs field" style="left:603px;top:958px;width:109px;height:27px">Name</div>
  <div class="abs field" style="left:720px;top:958px;width:108px;height:27px">Email</div>
  <div class="abs field" style="left:603px;top:991px;width:225px;height:58px">Message</div>
  <a class="abs btn send">Send Message</a>

  <div class="abs legal">All right are reserved by <span>lenahartwell.example</span></div>
</div>
</body>
</html>
```